brightquokka.net we need a webpage designed for our new product

We need a webpage designed for our new range of products from our new brand. We have had a logo designed on sketchhive (see attached) and we want to keep to this theme. Our first product is a range of affordable app controlled LED lightbulbs.

I have added some photos that we think is good inspirational material and would be good as a background to this website, but we want the site to look modern but not conventional. We would like something that makes our company look quirky not corporate.

Thats it

Target Market(s)

Our product is being stocked by big name online retailers in the UK, the page will get link through hits from our app. Our target market is gadget freaks of all ages.

Industry/Entity Type

It Company

Requirements
Must have
• We are going to need a help page, text to be uploaded next few days.

We need a contact page.

design my work on iOS and Android as most people will access page through their handset or tablet.
Should not have
• We do not want anything too corporate.

```html
<!DOCTYPE html>
<html lang="en">
<head>
<meta charset="utf-8">
<title>Bright Quokka – App Controlled LED Bulbs</title>
<link href="https://fonts.googleapis.com/css2?family=Raleway:wght@200;300;400;500;600&family=Open+Sans:wght@400;600;700&display=swap" rel="stylesheet">
<style>
  :root {
    --green-hero: #45a84a;
    --green-button: #5cb230;
    --green-text: #2f9e2f;
    --ink: #333333;
    --ink-soft: #555555;
    --white: #ffffff;
    --dark-button: #3b3b3b;
    --testimonial-bg: #3a3a3a;
    --featured-bg: #4b4e53;
    --featured-text: #9da1a6;
    --nav-active: #5a5a5a;
  }
  * { margin: 0; padding: 0; box-sizing: border-box; }
  html, body { width: 1200px; height: 2605px; overflow: hidden; }
  body { position: relative; background: var(--white); font-family: "Open Sans", sans-serif; color: var(--ink); }
  h1, h2, h3 { font-weight: 400; }
  .abs { position: absolute; }

  /* header */
  .site-header { position: absolute; left: 0; top: 0; width: 1200px; height: 182px; background: var(--white); }
  .brand { left: 130px; top: 44px; display: flex; align-items: center; gap: 12px; }
  .brand-dot { width: 30px; height: 30px; border-radius: 50%; background: var(--green-text); }
  .brand-name { font-weight: 700; font-size: 20px; color: var(--green-text); letter-spacing: 0.5px; }
  .language { left: 885px; top: 40px; display: flex; align-items: center; gap: 12px; font-size: 11px; color: #777; }
  .language .label { text-decoration: underline; }
  .language .current { font-size: 13px; color: #666; display: flex; align-items: center; gap: 6px; }
  .main-nav { left: 479px; top: 106px; display: flex; align-items: center; }
  .main-nav a { font-size: 13px; color: #333; text-decoration: none; padding: 9px 11px; margin-right: 5px; text-transform: uppercase; }
  .main-nav a.active { background: var(--nav-active); color: var(--white); border-radius: 2px; padding: 9px 19px; margin-right: 13px; }

  /* hero */
  .hero { position: absolute; left: 0; top: 182px; width: 1200px; height: 459px; background: radial-gradient(circle at 20% 80%, #52b457 0%, var(--green-hero) 45%, #3f9f44 100%); }
  .hero-title { left: 127px; top: 107px; font-family: "Raleway", sans-serif; font-weight: 400; font-size: 45px; color: var(--white); }
  .hero-sub { left: 130px; top: 178px; font-family: "Raleway", sans-serif; font-size: 24px; line-height: 31px; color: var(--white); }
  .btn-dark { left: 127px; top: 268px; width: 153px; height: 43px; background: var(--dark-button); color: var(--white); font-weight: 600; font-size: 15px; display: flex; align-items: center; justify-content: center; border-radius: 3px; }
  .slider-dots { display: flex; gap: 8px; }
  .slider-dots span { width: 9px; height: 9px; border-radius: 50%; background: var(--white); }
  .hero .slider-dots { left: 130px; top: 334px; }
  .hero-visual { left: 747px; top: 35px; width: 330px; height: 408px; border-radius: 30px; background: linear-gradient(160deg, #ffffff 0%, #d8d8d8 35%, #3a3a3a 75%, #222 100%); opacity: 0.9; }

  /* welcome */
  .welcome { position: absolute; left: 0; top: 641px; width: 1200px; height: 408px; background: var(--white); }
  .welcome-visual { left: 130px; top: 28px; width: 339px; height: 347px; border-radius: 24px; background: linear-gradient(160deg, #7ee07f 0%, #c9d3c9 40%, #3c3c3c 80%, #2a2a2a 100%); }
  .welcome-title { left: 541px; top: 56px; font-family: "Raleway", sans-serif; font-weight: 400; font-size: 45px; line-height: 50px; color: var(--ink); width: 520px; }
  .welcome-sub { left: 545px; top: 175px; font-family: "Raleway", sans-serif; font-size: 24px; line-height: 31px; color: var(--ink-soft); }
  .btn-green { height: 44px; background: var(--green-button); color: var(--white); font-weight: 600; font-size: 15px; display: flex; align-items: center; justify-content: center; border-radius: 2px; }
  .welcome .btn-green { left: 545px; top: 259px; width: 177px; }

  /* what we do */
  .services { position: absolute; left: 0; top: 1049px; width: 1200px; height: 512px; background: linear-gradient(180deg, #5a4f45 0%, #3b342f 45%, #4a4038 100%); }
  .services-title { left: 0; top: 30px; width: 1200px; text-align: center; font-family: "Raleway", sans-serif; font-weight: 500; font-size: 45px; color: var(--white); }
  .services-sub { left: 0; top: 94px; width: 1200px; text-align: center; font-size: 15px; color: var(--white); }
  .service { top: 172px; width: 260px; text-align: center; color: var(--white); }
  .service svg { display: block; margin: 0 auto; height: 90px; }
  .service h3 { font-family: "Raleway", sans-serif; font-weight: 400; font-size: 21px; margin-top: 30px; }
  .service p { font-size: 12px; line-height: 18px; margin: 8px auto 0; width: 232px; }

  /* colours */
  .colours { position: absolute; left: 0; top: 1561px; width: 1200px; height: 473px; background: var(--white); }
  .colours-title { left: 128px; top: 102px; font-family: "Raleway", sans-serif; font-weight: 400; font-size: 45px; line-height: 50px; color: var(--ink); }
  .colours-text { left: 128px; top: 227px; width: 520px; font-family: "Raleway", sans-serif; font-size: 17px; line-height: 30px; color: var(--ink-soft); }
  .colours .btn-green { left: 128px; top: 335px; width: 178px; }
  .colours-visual { left: 790px; top: 51px; width: 308px; height: 422px; border-radius: 28px 28px 0 0; background: linear-gradient(180deg, #1e1e1e 0%, #2a2a2a 20%, #d64a4a 40%, #4aa8d6 55%, #7ac24a 65%, #e8c0a8 85%, #e3b597 100%); }

  /* testimonials */
  .testimonials { position: absolute; left: 0; top: 2034px; width: 1200px; height: 432px; background: var(--testimonial-bg); color: var(--white); }
  .testimonials-title { left: 0; top: 18px; width: 1200px; text-align: center; font-family: "Raleway", sans-serif; font-weight: 200; font-size: 48px; }
  .testimonials-sub { left: 0; top: 92px; width: 1200px; text-align: center; font-size: 16px; line-height: 22px; }
  .arc { top: 198px; }
  .person-name { left: 184px; top: 204px; font-family: "Raleway", sans-serif; font-size: 31px; }
  .person-role { left: 184px; top: 245px; font-size: 16px; }
  .person-email { left: 184px; top: 270px; font-size: 13px; color: var(--green-button); text-decoration: underline; }
  .person-photo { left: 469px; top: 175px; width: 174px; height: 174px; border-radius: 50%; background: radial-gradient(circle at 50% 45%, #c89272 0%, #8a5a3e 55%, #3d6a3a 100%); }
  .quote { left: 693px; top: 220px; width: 340px; font-size: 15px; line-height: 21px; }
  .testimonials .slider-dots { left: 531px; top: 381px; }
  .testimonials .slider-dots span:first-child { width: 13px; height: 13px; margin-top: -2px; }

  /* featured */
  .featured { position: absolute; left: 0; top: 2466px; width: 1200px; height: 83px; background: var(--featured-bg); display: flex; align-items: center; justify-content: center; gap: 36px; color: var(--featured-text); }
  .featured .label { font-size: 9px; font-weight: 700; letter-spacing: 1px; }
  .featured .outlet { font-size: 17px; font-weight: 700; }

  /* footer */
  .site-footer { position: absolute; left: 0; top: 2549px; width: 1200px; height: 56px; background: var(--white); }
  .copyright { left: 127px; top: 20px; font-size: 13px; color: #555; }
  .social { left: 821px; top: 14px; display: flex; align-items: center; gap: 13px; font-size: 11px; color: #555; }
  .social .circle { width: 27px; height: 27px; border-radius: 50%; background: #3d3d3d; }
</style>
</head>
<body>

<header class="site-header">
  <div class="abs brand"><span class="brand-dot"></span><span class="brand-name">BRIGHTQUOKKA</span></div>
  <div class="abs language">
    <span class="label">Change Language</span>
    <span class="current">English
      <svg width="10" height="7" viewBox="0 0 10 7"><path d="M0 0 H10 L5 7 Z" fill="#4cae4c"/></svg>
    </span>
  </div>
  <nav class="abs main-nav">
    <a class="active">Home</a><a>About Us</a><a>Services</a><a>Store</a><a>Buy Now</a><a>Products</a><a>Contact Us</a>
  </nav>
</header>

<section class="hero">
  <h1 class="abs hero-title">Bright Quokka</h1>
  <p class="abs hero-sub">Control Led Buls Lights with App<br>Sit quet amet dolor lipsum</p>
  <div class="abs btn-dark">Read More</div>
  <div class="abs slider-dots"><span></span><span></span><span></span></div>
  <div class="abs hero-visual" role="img" aria-label="Smartphone showing the lighting app beside a glowing LED bulb"></div>
</section>

<section class="welcome">
  <div class="abs welcome-visual" role="img" aria-label="Green glowing LED bulb next to a smartphone with the lighting app"></div>
  <h2 class="abs welcome-title">Welcome to the Bright<br>Quokka</h2>
  <p class="abs welcome-sub">Control Led Buls Lights with App<br>Sit quet amet dolor lipsum</p>
  <div class="abs btn-green">Read More</div>
</section>

<section class="services" role="img" aria-label="Blurred photo of a shop interior behind the section">
  <h2 class="abs services-title">What We do</h2>
  <p class="abs services-sub">10 preset moods provide positive impact on your health.</p>

  <div class="abs service" style="left:122px">
    <svg viewBox="0 0 76 76" width="76"><g fill="#fff">
      <rect x="0" y="0" width="22" height="22" rx="3"/><rect x="27" y="0" width="22" height="22" rx="3"/><rect x="54" y="0" width="22" height="22" rx="3"/>
      <rect x="0" y="27" width="22" height="22" rx="3"/><rect x="27" y="27" width="22" height="22" rx="3"/><rect x="54" y="27" width="22" height="22" rx="3"/>
      <rect x="0" y="54" width="22" height="22" rx="3"/><rect x="27" y="54" width="22" height="22" rx="3"/><rect x="54" y="54" width="22" height="22" rx="3"/>
    </g></svg>
    <h3>APPLICATION</h3>
    <p>Experiment with millions of colors! Pick any color from the screen of your mobile lightbulb Glowen can transform conventional lighting into the night lights of Seattle or bring in the rich summer hues of Provence. Enliven your fantasies or raise your best memories in one click. Change the</p>
  </div>

  <div class="abs service" style="left:471px">
    <svg viewBox="0 0 90 90" width="90"><g fill="none" stroke="#fff" stroke-width="6">
      <path d="M45 8 C20 8 6 26 6 45 C6 66 22 82 42 82 C50 82 50 74 46 70 C42 64 46 58 54 58 H64 C76 58 80 48 80 40"/>
      <circle cx="26" cy="34" r="5"/><circle cx="40" cy="22" r="5"/><circle cx="24" cy="54" r="5"/>
      <path d="M84 6 L66 56" stroke-linecap="round"/></g></svg>
    <h3>LED &nbsp;COLOR</h3>
    <p>Experiment with millions of colors! Pick any color from the screen of your mobile lightbulb Glowen can transform conventional lighting into the night lights of Seattle or bring in the rich summer hues of Provence. Enliven your fantasies or raise your best memories in one click. Change the</p>
  </div>

  <div class="abs service" style="left:834px">
    <svg viewBox="0 0 60 120" width="55" style="height:120px;margin-top:-30px"><g fill="#fff">
      <rect x="6" y="0" width="48" height="12" rx="6"/><rect x="6" y="18" width="48" height="12" rx="6"/><rect x="6" y="36" width="48" height="12" rx="6"/><rect x="6" y="54" width="48" height="12" rx="6"/>
      <path d="M16 72 H44 L40 92 H20 Z"/><rect x="20" y="96" width="20" height="6" rx="2"/><rect x="22" y="106" width="16" height="6" rx="2"/><rect x="26" y="114" width="8" height="6" rx="2"/>
    </g></svg>
    <h3>LED &amp; LIGHT BULBS</h3>
    <p>Experiment with millions of colors! Pick any color from the screen of your mobile lightbulb Glowen can transform conventional lighting into the night lights of Seattle or bring in the rich summer hues of Provence. Enliven your fantasies or raise your best memories in one click. Change the</p>
  </div>
</section>

<section class="colours">
  <h2 class="abs colours-title">16 million Colors At your<br>FingerTips</h2>
  <p class="abs colours-text">Lumora is like going from black and white television to full-color HD. Imagine the ability to transform the ambience of your home or workplace using your smartphone.</p>
  <div class="abs btn-green">Read More</div>
  <div class="abs colours-visual" role="img" aria-label="Hand holding a smartphone showing a colour wheel in the lighting app"></div>
</section>

<section class="testimonials">
  <h2 class="abs testimonials-title">Testimonials</h2>
  <p class="abs testimonials-sub">Lorem ipsum dolor sit amet, consectetur adipisicing elit, sed<br>do eiusmod tempor incididunt ut labore et dolore magna</p>
  <svg class="abs arc" style="left:126px" width="30" height="160" viewBox="0 0 30 160"><path d="M28 2 C6 40 6 120 28 158" fill="none" stroke="#fff" stroke-width="2"/></svg>
  <svg class="abs arc" style="left:1046px" width="30" height="160" viewBox="0 0 30 160"><path d="M2 2 C24 40 24 120 2 158" fill="none" stroke="#fff" stroke-width="2"/></svg>
  <div class="abs person-name">Mira Halden</div>
  <div class="abs person-role">Accountant Manager</div>
  <div class="abs person-email">mira@quokkamail.net</div>
  <div class="abs person-photo" role="img" aria-label="Portrait photo of the customer"></div>
  <p class="abs quote">Lorem ipasum dolor sit amet, consectetur adipisicing elit, sed do eiusmod tempor incididunt ut labore et dolore magna aliqua. Ut enim ad minim veniam, quis nostrud exercitation</p>
  <div class="abs slider-dots"><span></span><span></span><span></span></div>
</section>

<section class="featured">
  <span class="label">FEATURED ON</span>
  <span class="outlet">Ledger</span>
  <span class="outlet">Circuit</span>
  <span class="outlet">Snapwire</span>
  <span class="outlet">NWB</span>
  <span class="outlet">Gadgetry</span>
  <span class="outlet">ByteDesk</span>
  <span class="outlet">unboxd</span>
</section>

<footer class="site-footer">
  <div class="abs copyright">©Bright Quokka. 2014</div>
  <div class="abs social">
    <span>Socialize With us :</span>
    <span class="circle"></span><span class="circle"></span><span class="circle"></span><span class="circle"></span>
  </div>
</footer>

</body>
</html>
```